Boutique Barre Studio in Geneva

Business card for pilates and dance studio. We are a brand new studio and love our fresh image with our yellow color. This business card is meant for our founder.

```html
<!DOCTYPE html>
<html lang="en">
<head>
<meta charset="utf-8">
<title>Poise Studio – Business Card</title>
<link href="https://fonts.googleapis.com/css2?family=Open+Sans:ital,wght@0,300;0,400;1,400&display=swap" rel="stylesheet">
<style>
  :root {
    --backdrop: #2c2c2e;
    --card-black: #1f1f21;
    --sun-yellow: #e7dd7d;
    --text-light: #c9c9c9;
    --text-dark: #2a2a2a;
    --text-muted: #4a4a4a;
    --mark-grey: #3a3a3d;
  }
  * { margin: 0; padding: 0; box-sizing: border-box; }
  html, body {
    width: 1200px; height: 1138px; overflow: hidden;
    background: var(--backdrop);
    font-family: "Open Sans", sans-serif;
  }
  .card {
    position: absolute;
    width: 620px; height: 374px;
    border-radius: 16px;
    background: var(--card-black);
    overflow: hidden;
  }
  .card-front { left: 274px; top: 186px; }
  .card-back  { left: 276px; top: 608px; }

  .front-brand {
    position: absolute; inset: 0;
    display: flex; align-items: center; justify-content: center; gap: 16px;
  }
  .front-brand .brand-dot {
    width: 22px; height: 22px; border-radius: 50%;
    background: var(--mark-grey);
  }
  .front-brand .brand-name {
    font-size: 46px; font-weight: 400; color: var(--mark-grey);
    letter-spacing: 1px;
  }

  .header-band {
    position: absolute; left: 0; top: 0;
    width: 620px; height: 130px;
    background: var(--sun-yellow);
  }

  .person {
    position: absolute; right: 30px; top: 40px; text-align: right;
  }
  .person-name { font-size: 22px; font-weight: 400; color: var(--text-dark); }
  .person-role { font-size: 15px; font-style: italic; color: var(--text-muted); margin-top: 2px; }

  .wordmark {
    position: absolute; left: 30px; top: 176px;
    font-size: 52px; font-weight: 400; color: var(--sun-yellow);
    line-height: 1; letter-spacing: 1px;
  }

  .address {
    position: absolute; left: 31px; top: 293px;
    font-size: 16px; font-weight: 300; color: var(--text-light); line-height: 25px;
  }
  .contacts {
    position: absolute; right: 28px; top: 268px;
    font-size: 16px; font-weight: 300; color: var(--text-light); line-height: 25px;
    text-align: right;
  }
  .contact-row { display: flex; align-items: center; justify-content: flex-end; gap: 10px; }
  .contact-row svg { width: 16px; height: 16px; }
</style>
</head>
<body>

<section class="card card-front">
  <div class="front-brand">
    <span class="brand-dot"></span>
    <span class="brand-name">poise</span>
  </div>
</section>

<section class="card card-back">
  <div class="header-band" role="img" aria-label="Yellow header area with a flowing wave ornament"></div>

  <div class="person">
    <div class="person-name">Mara Vellin</div>
    <div class="person-role">Founder</div>
  </div>

  <div class="wordmark">poise studio</div>

  <div class="address">
    <div>Rue des Alpes 12 1201</div>
    <div>Geneva, Switzerland</div>
  </div>

  <div class="contacts">
    <div class="contact-row">+33 600 482 915
      <svg viewBox="0 0 16 16"><circle cx="8" cy="8" r="7" fill="none" stroke="var(--sun-yellow)" stroke-width="1.4"/><path d="M5.5,4.5 L7,6 L6.2,7 C6.8,8.3 7.7,9.2 9,9.8 L10,9 L11.5,10.5 L10.5,11.6 C7.5,11 5,8.5 4.4,5.5 Z" fill="var(--sun-yellow)"/></svg>
    </div>
    <div class="contact-row">www.poise-barre.com
      <svg viewBox="0 0 16 16"><rect x="1.5" y="3.5" width="13" height="9" fill="none" stroke="var(--sun-yellow)" stroke-width="1.4"/><path d="M1.5,3.5 L8,9 L14.5,3.5" fill="none" stroke="var(--sun-yellow)" stroke-width="1.4"/></svg>
    </div>
    <div class="contact-row">hello@poise-barre.com
      <svg viewBox="0 0 16 16"><circle cx="8" cy="8" r="6.5" fill="none" stroke="var(--sun-yellow)" stroke-width="1.4"/><ellipse cx="8" cy="8" rx="3" ry="6.5" fill="none" stroke="var(--sun-yellow)" stroke-width="1.2"/><path d="M1.5,8 H14.5" stroke="var(--sun-yellow)" stroke-width="1.2"/></svg>
    </div>
  </div>
</section>

</body>
</html>
```